Flyer design to promote a new product (Chinese premium cooking sauce)

Task Outline
Create a flyer design
Task Description
We need to create a flyer to promote a new product (Chinese premium cooking sauce) in two languages (French/Chinese).
The flyer needs to include the following elements:
• Brand logo
• Product name
• Product description
• Two product-packaging images
• Three product benefits
• One unique selling point mark
Flyer Size
A5
Look & Feel
It needs to look modern, premium and Asian.
The color theme is Purple and Yellow (no specific PMS numbers are assigned.)
Please refer to the mood boards as well as the following websites:
http://www.velorabst.com/photos.html
http://dunmerofx.com/gallery/
Elegant
Serious
Modern
Professional
Feminine/Masculine
Conservative
Upmarket
Target Market(s)
Ethnic market: Chinese restaurants and takeaways in some of European markets (France, German and the Netherlands)
Industry/Entity Type
Cooking
Look and feel

```html
<!DOCTYPE html>
<html lang="fr">
<head>
<meta charset="utf-8">
<title>LUMAO – Sauce d'huître supérieure</title>
<link rel="stylesheet" href="https://fonts.googleapis.com/css2?family=Bebas+Neue&family=Noto+Sans+TC:wght@500;700&display=swap">
<style>
  :root {
    --ink: #2b2150;
    --ink-deep: #1f1840;
    --violet: #3e2f6e;
    --violet-soft: #564a80;
    --yellow: #f2ec3a;
    --yellow-soft: #e8e27a;
    --brand-red: #e2231a;
    --leaf: #5aa532;
  }
  * { margin: 0; padding: 0; box-sizing: border-box; }
  html, body { width: 848px; height: 1200px; overflow: hidden; background: var(--ink-deep); }
  .flyer {
    position: relative;
    width: 848px; height: 1200px; overflow: hidden;
    background:
      radial-gradient(ellipse 70% 55% at 45% 50%, var(--violet-soft) 0%, var(--violet) 45%, var(--ink-deep) 100%);
    font-family: "Bebas Neue", "Noto Sans TC", sans-serif;
  }
  .brush-band {
    position: absolute; left: 240px; top: 80px; width: 370px; height: 1060px;
    background: linear-gradient(180deg, var(--yellow-soft) 0%, var(--yellow) 30%, var(--yellow) 80%, var(--yellow-soft) 100%);
    border-radius: 40% 30% 35% 45% / 6% 4% 5% 8%;
    filter: blur(14px);
    opacity: 0.95;
  }
  .brand {
    position: absolute; left: 48px; top: 46px;
    display: flex; align-items: center; gap: 10px;
  }
  .brand-mark { width: 40px; height: 40px; background: var(--brand-red); }
  .brand-name {
    font-family: "Bebas Neue", sans-serif; font-size: 46px; line-height: 1;
    color: var(--yellow); letter-spacing: 2px;
  }
  .hero-title {
    position: absolute; left: 316px; top: 100px; width: 200px;
    font-family: "Noto Sans TC", sans-serif; font-weight: 500;
    font-size: 190px; line-height: 198px; text-align: center;
    color: var(--ink);
  }
  .hero-title span { display: block; }
  .info { position: absolute; left: 648px; top: 34px; width: 174px; }
  .tag {
    display: block; text-align: right; padding: 0 4px;
    margin-bottom: 4px; white-space: nowrap; overflow: hidden;
  }
  .tag--yellow { background: var(--yellow); color: var(--ink); }
  .tag--violet { background: var(--violet); color: var(--yellow); }
  .name-line { font-size: 74px; line-height: 64px; height: 64px; letter-spacing: -1px; }
  .name-zh {
    font-family: "Noto Sans TC", sans-serif; font-weight: 500;
    font-size: 30px; line-height: 64px; height: 64px; text-align: center;
  }
  .desc { font-size: 17px; line-height: 30px; height: 30px; text-align: center; }
  .benefits {
    list-style: none; background: var(--yellow); color: var(--ink);
    font-size: 13px; line-height: 17px; padding: 6px 6px; margin-top: 6px;
  }
  .benefits li { white-space: nowrap; }
  .benefits li::before { content: "• "; }
  .benefits-zh {
    position: absolute; left: 758px; top: 446px; width: 64px;
    background: var(--yellow); color: var(--ink);
    font-family: "Noto Sans TC", sans-serif; font-weight: 500;
    font-size: 14px; line-height: 20px; text-align: center; padding: 2px 0;
  }
  .usp-mark {
    position: absolute; left: 32px; top: 1108px; width: 78px; height: 78px;
    border-radius: 50%; background: var(--leaf);
  }
</style>
</head>
<body>
<main class="flyer">
  <div class="brush-band" role="img" aria-label="Yellow ink brush stroke on purple watercolour texture"></div>

  <div class="brand">
    <span class="brand-mark"></span>
    <span class="brand-name">LUMAO</span>
  </div>

  <h1 class="hero-title" lang="zh-Hant">
    <span>臻</span><span>選</span><span>金</span><span>蠔</span><span>油</span>
  </h1>

  <section class="info">
    <span class="tag tag--yellow name-line">SUPERB</span>
    <span class="tag tag--yellow name-line">OYSTER</span>
    <span class="tag tag--violet name-line">SAUCE</span>
    <span class="tag tag--yellow name-zh" lang="zh-Hant">臻選金蠔油</span>
    <span class="tag tag--violet desc">SAUCE D'HUÎTRE SUPÉRIEURE</span>
    <span class="tag tag--violet desc">ÉLABORÉE AVEC DU SUCRE BRUN</span>
    <ul class="benefits">
      <li>RICHE EN UMAMI</li>
      <li>RÉVÈLE LES COULEURS DE VOS PLATS</li>
      <li>POUR UNE CUISINE SAINE</li>
    </ul>
  </section>

  <div class="benefits-zh" lang="zh-Hant">鮮味提升<br>色澤豐潤<br>健康加分</div>

  <div class="usp-mark" role="img" aria-label="Quality seal: no preservatives or artificial colours"></div>
</main>
</body>
</html>
```